Signage setout with photos for side of Mowing Trailer

We need signage for our mowing trailer to attract new business.
Specifically a Rear sign 1470x880mm and Side signs 2400x880mm
Sign needs to be modern and professional.
Some example uploads as to what we have thought about so far.
Logo doesn't need to be the green colour.
Logo words and Logo of Mower do not need to be together.
Link to get a mower image>
https://bluefernmachinery.com/torvo
Updates

Need extra days to review

Target Market(s)

Other Customers driving past the trailer.

Industry/Entity Type

Lawnmowing / Landscaping

Requirements
Must have
• Phone Number, Company Name & Logo, Web address, Facebook and Insta Logos, Comment - "Acreage & Commercial Specialists" Catchcry - "100% Electric Mowing Company - est 2017" Services "Mowing, Hedging, Pressure Cleaning, Weed Control, Fencing, Turfing, Mulching and Rubbish Removal"
Nice to have
• Full colour background images.

```html
<!DOCTYPE html>
<html lang="en">
<head>
<meta charset="utf-8">
<title>Fresh Cut Mowing – Trailer Sign</title>
<link rel="stylesheet" href="https://fonts.googleapis.com/css2?family=Bitter:wght@700;800&family=Mulish:ital,wght@1,900&display=swap">
<style>
  :root {
    --page: #f1f1ed;
    --white: #ffffff;
    --brand-green: #0d7a3e;
    --band-green: #0f7a45;
    --orange: #ef7b44;
    --orange-deep: #e16a30;
    --grass-light: #6fc23a;
    --grass-mid: #3f9a22;
    --grass-dark: #236a12;
    --mower-green: #55c43a;
    --mower-dark: #2e5a24;
    --night: rgba(10, 20, 10, 0.88);
    --social: #ffffff;
  }
  * { margin: 0; padding: 0; box-sizing: border-box; }
  html, body { width: 1200px; height: 818px; overflow: hidden; background: var(--page); }
  .sign {
    position: absolute; left: 20px; top: 62px;
    width: 1160px; height: 694px; overflow: hidden;
  }
  .sign-shapes { position: absolute; inset: 0; width: 1160px; height: 694px; }
  .brand-name {
    position: absolute; left: 70px; top: 100px; width: 270px;
    font-family: "Bitter", serif; font-weight: 800; color: var(--brand-green);
    text-align: center; line-height: 1.05; font-size: 36px; letter-spacing: 0.5px;
  }
  .brand-name .brand-line-two { font-size: 42px; }
  .brand-dot {
    position: absolute; left: 180px; top: 34px; width: 50px; height: 50px;
    border-radius: 50%; background: var(--orange);
  }
  .web-address {
    position: absolute; left: 23px; top: 240px;
    font-family: "Mulish", sans-serif; font-style: italic; font-weight: 900;
    font-size: 23px; color: var(--white); letter-spacing: 0.3px;
  }
  .headline, .tagline, .phone {
    position: absolute; font-family: "Bitter", serif; font-weight: 800;
    color: var(--white); text-align: center; white-space: nowrap;
    text-shadow: 2px 3px 4px rgba(0,0,0,0.35);
  }
  .headline { left: 720px; width: 400px; top: 32px; font-size: 62px; line-height: 80px; }
  .tagline { left: 20px; width: 440px; top: 334px; font-size: 54px; line-height: 71px; }
  .phone {
    left: 800px; width: 330px; top: 335px; font-size: 60px;
    color: var(--orange); -webkit-text-stroke: 7px var(--white); paint-order: stroke fill;
    text-shadow: none; letter-spacing: 1px;
  }
  .socials { position: absolute; left: 908px; top: 409px; display: flex; gap: 28px; }
  .social-dot { width: 42px; height: 42px; border-radius: 50%; background: var(--social); opacity: 0.9; }
  .services {
    position: absolute; left: 32px; width: 1095px; top: 644px;
    display: flex; justify-content: space-between; list-style: none;
    font-family: "Bitter", serif; font-weight: 700; font-size: 18.5px; color: var(--white);
    white-space: nowrap;
  }
  .services li::before { content: "• "; }
</style>
</head>
<body>
  <main class="sign">
    <svg class="sign-shapes" viewBox="0 0 1788 1070" preserveAspectRatio="none">
      <defs>
        <linearGradient id="grass" x1="0" y1="0" x2="0.3" y2="1">
          <stop offset="0" stop-color="var(--grass-light)"/>
          <stop offset="0.55" stop-color="var(--grass-mid)"/>
          <stop offset="1" stop-color="var(--grass-dark)"/>
        </linearGradient>
        <linearGradient id="mower" x1="0" y1="0" x2="0" y2="1">
          <stop offset="0" stop-color="var(--mower-dark)"/>
          <stop offset="0.5" stop-color="var(--mower-green)"/>
          <stop offset="1" stop-color="var(--mower-dark)"/>
        </linearGradient>
      </defs>
      <rect class="grass-photo" x="0" y="0" width="1788" height="1070" fill="url(#grass)" role="img" aria-label="Photo of a freshly mown green lawn"/>
      <polygon class="panel-white" points="0,0 970,0 685,357 0,357" fill="var(--white)"/>
      <polygon class="band-web" points="0,357 745,357 805,432 0,432" fill="var(--band-green)"/>
      <polygon class="panel-orange" points="0,432 865,432 1315,1070 0,1070" fill="var(--orange)"/>
      <polygon class="panel-orange-shade" points="615,432 865,432 1315,1070 330,1070 330,968" fill="var(--orange-deep)"/>
      <rect class="services-bar-left" x="0" y="968" width="1315" height="102" fill="rgba(0,0,0,0.05)"/>
      <polygon class="services-bar-right" points="1243,968 1788,968 1788,1070 1315,1070" fill="var(--night)"/>
      <polygon class="mower-photo" points="870,180 1070,180 1120,440 1300,700 1445,760 1445,968 600,968 700,760 870,700" fill="url(#mower)" opacity="0.85" role="img" aria-label="Cut-out photo of an operator riding a green electric zero-turn mower"/>
    </svg>

    <div class="brand-dot"></div>
    <div class="brand-name"><div>FRESH CUT</div><div class="brand-line-two">MOWING</div></div>
    <div class="web-address">www.freshcutmowing.com.au</div>

    <h1 class="headline">Acreage &amp;<br>Commercial<br>Specialists</h1>
    <p class="tagline">100% Electric<br>Mowing Company<br>- est 2017</p>
    <p class="phone">3555 0142</p>
    <div class="socials"><span class="social-dot"></span><span class="social-dot"></span></div>

    <ul class="services">
      <li>Mowing</li>
      <li>Hedging</li>
      <li>Pressure Cleaning</li>
      <li>Weed Control</li>
      <li>Fencing</li>
      <li>Turfing</li>
      <li>Mulching and Rubbish Removal</li>
    </ul>
  </main>
</body>
</html>
```